Business Cards

Business card design for my company.
I would like the card's background colour to be black. You can also see our web site to get an idea of our brand. https://www.dlqmarrowfield.com.au/
- Name
- Email

```html
<!DOCTYPE html>
<html lang="en">
<head>
<meta charset="utf-8">
<title>DLQ Marrowfield – Business Cards</title>
<link href="https://fonts.googleapis.com/css2?family=Montserrat:wght@400;500;700;800&display=swap" rel="stylesheet">
<style>
  :root {
    --canvas: #2b2b2b;
    --card: #050505;
    --brand-green: #1a9a4a;
    --ink: #ffffff;
    --ink-soft: #e6e6e6;
  }
  * { margin: 0; padding: 0; box-sizing: border-box; }
  html, body { width: 1200px; height: 875px; overflow: hidden; }
  body {
    background: var(--canvas);
    font-family: "Montserrat", sans-serif;
    display: flex;
    align-items: center;
    justify-content: center;
    gap: 60px;
  }
  .card {
    width: 525px;
    height: 300px;
    background: var(--card);
    border-radius: 18px;
    position: relative;
    box-shadow: 0 20px 40px rgba(0,0,0,0.45);
  }
  .card--front {
    display: flex;
    align-items: center;
    justify-content: center;
  }
  .wordmark {
    display: flex;
    align-items: center;
    gap: 14px;
  }
  .wordmark__mark {
    width: 18px;
    height: 18px;
    background: var(--brand-green);
  }
  .wordmark__name {
    font-weight: 800;
    font-size: 34px;
    letter-spacing: 0.04em;
    color: var(--ink);
    text-transform: uppercase;
  }
  .card--back .wordmark {
    position: absolute;
    top: 44px;
    right: 40px;
  }
  .card--back .wordmark__name { font-size: 24px; }
  .card--back .wordmark__mark { width: 13px; height: 13px; }
  .contact {
    position: absolute;
    left: 40px;
    bottom: 36px;
  }
  .contact__name {
    font-weight: 700;
    font-size: 24px;
    color: var(--ink);
    line-height: 1.1;
  }
  .contact__name .first { color: var(--brand-green); }
  .contact__role {
    font-size: 12px;
    color: var(--ink-soft);
    margin: 3px 0 12px;
  }
  .contact__list { list-style: none; }
  .contact__item {
    display: flex;
    align-items: center;
    gap: 10px;
    font-size: 12px;
    color: var(--ink-soft);
    margin-top: 6px;
  }
  .contact__icon { width: 13px; height: 13px; flex: none; }
</style>
</head>
<body>
  <section class="card card--front" aria-label="Card front">
    <div class="wordmark">
      <span class="wordmark__mark"></span>
      <span class="wordmark__name">DLQ Marrowfield</span>
    </div>
  </section>

  <section class="card card--back" aria-label="Card back">
    <div class="wordmark">
      <span class="wordmark__mark"></span>
      <span class="wordmark__name">DLQ Marrowfield</span>
    </div>
    <div class="contact">
      <p class="contact__name"><span class="first">Mara</span> Jensen</p>
      <p class="contact__role">Managing Director</p>
      <ul class="contact__list">
        <li class="contact__item">
          <svg class="contact__icon" viewBox="0 0 16 16" fill="var(--brand-green)"><path d="M3.6 1.5l2.3 2.3-1.3 2a9 9 0 0 0 5 5l2-1.3 2.3 2.3-1.6 2.2C7.4 15.2.8 8.6 1.4 3.1z"/></svg>
          (08) 9400 2817
        </li>
        <li class="contact__item">
          <svg class="contact__icon" viewBox="0 0 16 16" fill="var(--brand-green)"><path d="M1 3h14v10H1z"/><path d="M1 3l7 6 7-6" stroke="#050505" stroke-width="1.4" fill="none"/></svg>
          info@dlqmarrowfield.com.au
        </li>
        <li class="contact__item">
          <svg class="contact__icon" viewBox="0 0 16 16" fill="none" stroke="var(--brand-green)" stroke-width="1.6"><circle cx="8" cy="8" r="6.5"/><path d="M1.5 8h13M8 1.5c-3 3.5-3 9.5 0 13M8 1.5c3 3.5 3 9.5 0 13"/></svg>
          www.dlqmarrowfield.com.au
        </li>
      </ul>
    </div>
  </section>
</body>
</html>
```